Company director needs a business card design

I am a semi-retired former senior finance executive who sits on a number of public and private company boards and do some consulting work. I work largely with emerging businesses but deal regularly with top end of town lawyers, bankers etc. I need a thoughtful but relatively conservative design which would also resonate with my younger client base. Some colour would be good. Information limited to name, address, office tel, mobile and email.

Industry/Entity Type

Finance

```html
<!DOCTYPE html>
<html lang="en">
<head>
<meta charset="utf-8">
<title>Business Card – Front and Back</title>
<link href="https://fonts.googleapis.com/css2?family=Cinzel:wght@400&family=Didact+Gothic&display=swap" rel="stylesheet">
<style>
  :root {
    --bg: #e8e7e3;
    --card: #ffffff;
    --green-dark: #0b6210;
    --green-bright: #2de80a;
    --ink: #111111;
    --shadow: rgba(0,0,0,0.18);
  }
  * { margin: 0; padding: 0; box-sizing: border-box; }
  html, body { width: 1200px; height: 800px; overflow: hidden; }
  body {
    background: var(--bg);
    position: relative;
  }
  .card {
    position: absolute;
    left: 280px;
    width: 640px;
    height: 366px;
    background: var(--card);
    box-shadow: 0 6px 18px var(--shadow);
    overflow: hidden;
  }
  .card--front { top: 24px; }
  .card--back { top: 410px; }
  .card__bands {
    position: absolute;
    inset: 0;
    width: 100%;
    height: 100%;
  }
  .card__name {
    position: absolute;
    font-family: "Cinzel", serif;
    font-size: 27px;
    letter-spacing: 1px;
    color: var(--ink);
    white-space: nowrap;
  }
  .card--front .card__name { left: 64px; top: 150px; }
  .card--back .card__name { left: 40px; top: 150px; }
  .contact {
    position: absolute;
    left: 356px;
    top: 110px;
    list-style: none;
    font-family: "Didact Gothic", sans-serif;
    font-size: 18px;
    line-height: 1.25;
    color: var(--ink);
    white-space: nowrap;
  }
  .contact__item {
    display: flex;
    align-items: flex-start;
    margin-bottom: 10px;
  }
  .contact__icon {
    flex: 0 0 18px;
    width: 18px;
    height: 18px;
    margin-right: 14px;
    margin-top: 2px;
    fill: var(--ink);
  }
</style>
</head>
<body>

  <!-- Front: name face -->
  <section class="card card--front" aria-label="Card front">
    <svg class="card__bands" viewBox="0 0 640 366" aria-hidden="true">
      <defs>
        <linearGradient id="divider-front" x1="0" y1="0" x2="0" y2="1">
          <stop offset="0" stop-color="#0b6210"/>
          <stop offset="1" stop-color="#2de80a"/>
        </linearGradient>
      </defs>
      <polygon points="0,0 400,0 360,44 0,44" fill="var(--green-dark)"/>
      <polygon points="420,0 640,0 640,24 405,24" fill="var(--green-bright)"/>
      <polygon points="0,318 300,318 330,340 640,340 640,366 0,366" fill="var(--green-bright)"/>
      <line x1="372" y1="100" x2="340" y2="270" stroke="url(#divider-front)" stroke-width="3"/>
    </svg>
    <p class="card__name">Your Name</p>
  </section>

  <!-- Back: contact face -->
  <section class="card card--back" aria-label="Card back">
    <svg class="card__bands" viewBox="0 0 640 366" aria-hidden="true">
      <defs>
        <linearGradient id="divider-back" x1="0" y1="0" x2="0" y2="1">
          <stop offset="0" stop-color="#0b6210"/>
          <stop offset="1" stop-color="#2de80a"/>
        </linearGradient>
      </defs>
      <polygon points="0,0 330,0 370,42 0,42" fill="var(--green-dark)"/>
      <polygon points="380,0 640,0 640,30 400,30" fill="var(--green-bright)"/>
      <polygon points="0,322 260,322 290,344 0,344" fill="var(--green-bright)"/>
      <polygon points="0,344 300,344 300,366 0,366" fill="var(--green-bright)"/>
      <polygon points="300,366 300,332 330,310 640,310 640,366" fill="var(--green-dark)"/>
      <line x1="334" y1="78" x2="296" y2="286" stroke="url(#divider-back)" stroke-width="3"/>
    </svg>
    <p class="card__name">Your Name</p>
    <ul class="contact">
      <li class="contact__item">
        <svg class="contact__icon" viewBox="0 0 24 24" aria-hidden="true"><path d="M6.6 10.8a15.2 15.2 0 0 0 6.6 6.6l2.2-2.2a1 1 0 0 1 1-.25 11.4 11.4 0 0 0 3.6.57 1 1 0 0 1 1 1V20a1 1 0 0 1-1 1A17 17 0 0 1 3 4a1 1 0 0 1 1-1h3.5a1 1 0 0 1 1 1c0 1.25.2 2.45.57 3.57a1 1 0 0 1-.25 1z"/></svg>
        <span>+1 (555) 0142 736</span>
      </li>
      <li class="contact__item">
        <svg class="contact__icon" viewBox="0 0 24 24" aria-hidden="true"><path d="M7 2h10a2 2 0 0 1 2 2v16a2 2 0 0 1-2 2H7a2 2 0 0 1-2-2V4a2 2 0 0 1 2-2zm0 3v13h10V5z"/></svg>
        <span>+1 (555) 0198 204</span>
      </li>
      <li class="contact__item">
        <svg class="contact__icon" viewBox="0 0 24 24" aria-hidden="true"><path d="M12 2a7 7 0 0 0-7 7c0 5.2 7 13 7 13s7-7.8 7-13a7 7 0 0 0-7-7zm0 9.5A2.5 2.5 0 1 1 12 6.5a2.5 2.5 0 0 1 0 5z"/></svg>
        <span>48 Harbour Lane, Millbrook,<br>NY 10041<br>P.O. Box: 207519</span>
      </li>
      <li class="contact__item">
        <svg class="contact__icon" viewBox="0 0 24 24" aria-hidden="true"><path d="M2 5h20v14H2zm2 2v.4l8 5.2 8-5.2V7z"/></svg>
        <span>office@mailbox.com</span>
      </li>
    </ul>
  </section>

</body>
</html>
```